1. Overview of company:
Copper Fern Mobile solutions private Ltd is one of the leading innovators & providers of Value added services (VAS) and telecom solutions to the top telecom operators across the world. We are the pioneer of several telecom technologies and products with our solutions empowering over 40 telecom giant in 51 countries.

2. Product Overview:
Vocal Twist is the most innovative voice morphing mobile app that has revolutionized the concept of IVR based offerings for telecom operators across the world. It lets you talk to your friend in a voice of your choice at just the press of a button. In addition to every call, users can now speak to their friends with background sounds of their choice.

In simple words: If person A calls person B, person A can choose the voice he wants B to listen, Words and sentences remain same just the voice changes. Person A can even activate a background sound for both of them while talking.

3. Objective of the design:
The purpose of this campaign is to establish Vocal Twist as Innovative, Lively, Youthful, Fun mobile app generally used for spreading smiles via pranks. The primary objective is to persuade the audience to download and use Vocal Twist mobile app, as well as to spread and characterize this new app.

4. Product layout:
Page 1: Landing Page
- pictorial explanation, what Vocal Twist stands for

Page 2: Home Screen options
-Navigation to vocal twist
-Navigation to sound scenery

Page 3: Vocal Twist options
-Female
-Cartoon
-King
-Bunny

Page 4: Sound scenery options
-Romantic
-Airport
-Traffic
-Football
-Church
-Beach

5. Target Audience
The users of the mobile app will be teenager whose age ranges from 16-27. The demographics are not restricted to a particular country and will be present on global level.

6. Deliverable
- 4 Uncoded screen and icon for mobile app "Vocal Twist"
- Our company name is "Copper Fern" , we would like to see designs that use Black and Green, at the same time its not mandatory.
-Design should communicate what the app stands for "Changing voice of caller"

Target Market(s)

User of the mobile app will be teenagers whose age ranges from 16-27. The demographics are not restricted to a particular country and will be present on global level. It's for masses.

Industry/Entity Type

Telecommunications

Requirements
Must have
• The design should be self explanatory, what the app stands for.
• Editable format for integration purpose.
Nice to have
• Would prefer Icons and very few words.
• Professional, elegant at the same time trendy designs.

```html
<!DOCTYPE html>
<html lang="en">
<head>
<meta charset="utf-8">
<title>Sound Scenery Options</title>
<link rel="stylesheet" href="https://fonts.googleapis.com/css2?family=Open+Sans:wght@700&display=swap">
<style>
  :root {
    --status-bg: #0a0a0a;
    --header-bg: #1f1f1f;
    --accent: #1ccb2f;
    --icon-green: #129a2e;
    --label: #222222;
    --page: #ffffff;
    --status-icon: #9a9a9a;
    --white: #ffffff;
  }
  * { margin: 0; padding: 0; box-sizing: border-box; }
  html, body { width: 1200px; height: 2715px; overflow: hidden; background: var(--page); }
  .screen { position: relative; width: 1200px; height: 2715px; background: var(--page); font-family: "Open Sans", Arial, sans-serif; }
  .status-bar { position: absolute; left: 0; top: 0; width: 1200px; height: 75px; background: var(--status-bg); }
  .status-bar svg { position: absolute; }
  .app-header { position: absolute; left: 0; top: 75px; width: 1200px; height: 628px; background: var(--header-bg); }
  .menu-button { position: absolute; left: 58px; top: 45px; }
  .more-button { position: absolute; left: 1122px; top: 42px; }
  .title-ring {
    position: absolute; left: 381px; top: 112px; width: 420px; height: 420px;
    border: 5.6px solid var(--accent); border-radius: 50%;
    display: flex; align-items: center; justify-content: center; text-align: center;
  }
  .title-ring h1 { color: var(--accent); font-size: 44px; font-weight: 700; line-height: 54px; letter-spacing: 0.3px; }
  .scenery-option { position: absolute; left: 0; width: 1200px; }
  .scenery-option svg { position: absolute; fill: var(--icon-green); }
  .scenery-option .label {
    position: absolute; font-size: 68px; font-weight: 700; color: var(--label);
    line-height: 90px; letter-spacing: 2px; white-space: nowrap;
  }
</style>
</head>
<body>
<div class="screen">
  <div class="status-bar">
    <svg width="90" height="40" viewBox="0 0 48 21" style="left:15px;top:17px" fill="var(--status-icon)">
      <rect x="0" y="12" width="6" height="8"/><rect x="8" y="10" width="6" height="10"/>
      <rect x="16" y="7" width="6" height="13"/><rect x="24" y="4" width="6" height="16"/><rect x="32" y="0" width="6" height="20"/>
    </svg>
    <svg width="80" height="36" viewBox="0 0 42 19" style="left:1110px;top:18px">
      <rect x="1" y="1" width="36" height="17" fill="none" stroke="var(--status-icon)" stroke-width="1.5"/>
      <rect x="3.5" y="3.5" width="31" height="12" fill="var(--status-icon)"/>
      <rect x="38" y="6" width="3" height="7" fill="var(--status-icon)"/>
    </svg>
  </div>

  <header class="app-header">
    <svg class="menu-button" width="90" height="66" viewBox="0 0 90 66" fill="var(--white)">
      <rect x="0" y="0" width="90" height="7.5"/><rect x="0" y="29" width="90" height="7.5"/><rect x="0" y="58" width="90" height="7.5"/>
    </svg>
    <svg class="more-button" width="20" height="84" viewBox="0 0 20 84" fill="var(--white)">
      <circle cx="10" cy="10" r="9"/><circle cx="10" cy="41" r="9"/><circle cx="10" cy="73" r="9"/>
    </svg>
    <div class="title-ring"><h1>Sound Scenery<br>Options</h1></div>
  </header>

  <div class="scenery-option">
    <svg width="203" height="167" viewBox="0 0 108 89" style="left:276px;top:876px">
      <path d="M54 89C40 78 0 55 0 28C0 12 12 0 28 0C40 0 50 8 54 16C58 8 68 0 80 0C96 0 108 12 108 28C108 55 68 78 54 89Z"/>
    </svg>
    <span class="label" style="left:548px;top:909px">Romantic</span>
  </div>

  <div class="scenery-option">
    <svg width="205" height="205" viewBox="0 0 109 109" style="left:281px;top:1157px">
      <path d="M48.5 9C48.5 3 51 0 54.5 0S60.5 3 60.5 9V40L109 66V80L60.5 68V90L72 97V109L54.5 105L37 109V97L48.5 90V68L0 80V66L48.5 40Z"/>
    </svg>
    <span class="label" style="left:557px;top:1232px">Airport</span>
  </div>

  <div class="scenery-option">
    <svg width="169" height="141" viewBox="0 0 90 75" style="left:302px;top:1506px">
      <path fill-rule="evenodd" d="M20 0H70L80 20L86 28C89 31 90 34 90 38V60H75V75H60V60H30V75H15V60H0V38C0 34 1 31 4 28L10 20ZM21 6L14 22H76L69 6Z M6 42L20 46V42L7 38Z M84 42L70 46V42L83 38Z M31 41H59L56 49H34Z"/>
      <path d="M46 18L60 8" stroke="var(--icon-green)" stroke-width="1.5"/>
    </svg>
    <span class="label" style="left:562px;top:1537px">Traffic</span>
  </div>

  <div class="scenery-option">
    <svg width="208" height="174" viewBox="0 0 111 93" style="left:272px;top:1817px">
      <rect x="9" y="4" width="2" height="20"/><path d="M11 4L21 9L11 14Z"/>
      <rect x="54" y="0" width="2" height="20"/><path d="M56 0L66 5L56 10Z"/>
      <rect x="98" y="4" width="2" height="20"/><path d="M100 4L110 9L100 14Z"/>
      <path fill-rule="evenodd" d="M55.5 18C85 18 111 22 111 28C111 34 85 38 55.5 38C26 38 0 34 0 28C0 22 26 18 55.5 18ZM55.5 24C32 24 14 26 14 28.5C14 31 32 33 55.5 33C79 33 97 31 97 28.5C97 26 79 24 55.5 24Z"/>
      <path d="M1 34C20 41 91 41 110 34L107 52C105 64 93 70 75 73V62H36V73C18 70 6 64 4 52Z"/>
      <path d="M39 65H72V88H77V93H34V88H39ZM43 68V81H68V68Z"/>
    </svg>
    <span class="label" style="left:564px;top:1864px">Football</span>
  </div>

  <div class="scenery-option">
    <svg width="158" height="195" viewBox="0 0 84 104" style="left:304px;top:2085px">
      <path fill-rule="evenodd" d="M39 0H45V7H52V12H45V18L58 32H52V48L84 74H74V104H52V88C52 82 48 78 42 78C36 78 32 82 32 88V104H10V74H0L32 48V32H26L39 18V12H32V7H39ZM39 38V48H45V38C45 36 39 36 39 38Z"/>
    </svg>
    <span class="label" style="left:566px;top:2171px">Church</span>
  </div>

  <div class="scenery-option">
    <svg width="161" height="178" viewBox="0 0 86 95" style="left:306px;top:2423px">
      <path d="M0 95C0 88 14 80 43 80C72 80 86 88 86 95Z"/>
      <path d="M5 90C8 60 20 32 33 16L37 19C26 36 16 62 14 90Z"/>
      <path d="M33 16C28 8 18 4 10 8C18 8 24 12 27 18C20 14 12 16 8 22C16 19 24 20 31 22C26 26 22 34 23 42C28 32 33 26 37 22C40 28 40 38 36 46C44 40 46 30 43 22C52 24 60 32 62 40C64 28 56 20 46 18C54 14 64 16 70 20C66 10 54 8 44 12C44 6 40 1 34 0C38 5 38 10 36 14Z"/>
      <path d="M48 82C48 74 49 68 52 62L54 63C52 69 51 75 51 82Z"/>
      <path d="M52 62C48 58 42 58 38 62C43 61 47 62 50 64C46 65 42 69 41 73C45 69 49 66 53 65C55 68 55 72 54 75C58 72 58 67 56 64C60 64 64 67 66 70C66 65 62 62 57 61C60 58 64 57 68 58C65 54 59 54 55 58C55 55 53 52 50 52C52 55 52 58 52 62Z"/>
    </svg>
    <span class="label" style="left:572px;top:2497px">Beach</span>
  </div>
</div>
</body>
</html>
```